Business Card for a new businees.

need a very good business for a new company based in Riverside California call Levy Lantern LLC. We help client file taxes, resolve tax debt and attain peace of mind We help people nationwide solve Tax problems. We help with Installment agreements, Offers in Compromise, Partial Pay Installment Agreements, Currently Not Collectible status, Liens and Levy Removal, Garnishment removal. We offer individualized services

Target Market(s)

Any one with Tax Problems nationwide. My clients span across age, occupation etc

Contact Information for Business Card

Card must be attractive and have enough information to let client know we care and call us

Colors

Designer to choose colors to be used in the design.

Requirements
Must have
• the basics and then surprise me
Nice to have
• surprise m

```html
<!DOCTYPE html>
<html lang="en">
<head>
<meta charset="utf-8">
<title>Levy Lantern LLC — Business Card</title>
<link href="https://fonts.googleapis.com/css2?family=Roboto:wght@400;500;700&display=swap" rel="stylesheet">
<style>
  :root {
    --backdrop: #e9e6e1;
    --card-white: #f7f7f5;
    --band-black: #231f20;
    --gold: #9a8a1e;
    --gold-bright: #d9bf2a;
    --gold-deep: #958418;
    --gold-center: #f0d244;
    --ink: #2a2a2a;
    --ink-soft: #4a4a4a;
    --white: #ffffff;
  }
  html, body {
    margin: 0;
    width: 1200px;
    height: 960px;
    overflow: hidden;
    background: var(--backdrop);
    font-family: "Roboto", Arial, sans-serif;
  }
  .canvas { position: relative; width: 1200px; height: 960px; }

  .card {
    position: absolute;
    width: 600px;
    height: 342px;
    overflow: hidden;
    box-shadow: 0 3px 8px rgba(0,0,0,0.25);
  }

  /* Front */
  .card--front { left: 322px; top: 108px; background: var(--card-white); }
  .front__band {
    position: absolute; left: 0; top: 0; width: 70px; height: 100%;
    background: var(--band-black);
  }
  .brand { position: absolute; left: 16px; top: 32px; }
  .brand__row { display: flex; align-items: center; gap: 12px; }
  .brand__dot {
    width: 88px; height: 88px; border-radius: 50%;
    background: var(--gold-bright);
  }
  .brand__text { margin-top: 8px; }
  .brand__name {
    font-weight: 700; font-size: 32px; line-height: 1;
    color: var(--gold-bright); letter-spacing: -0.5px;
  }
  .brand__tagline {
    margin-top: 14px;
    font-size: 7.5px; font-weight: 700; letter-spacing: 1.2px;
    color: var(--ink);
  }
  .brand__subline {
    margin-top: 3px;
    font-size: 5.5px; font-weight: 700; letter-spacing: 0.2px;
    color: var(--gold);
  }

  .contact {
    position: absolute; right: 30px; top: 168px;
    text-align: right; color: var(--ink-soft);
  }
  .contact__name {
    font-size: 20px; font-weight: 500; color: var(--gold); line-height: 1.1;
  }
  .contact__role {
    font-size: 15px; font-weight: 500; color: var(--ink);
    margin-top: 2px; letter-spacing: 0.5px;
  }
  .contact__address { margin-top: 8px; font-size: 14.5px; line-height: 19px; }
  .contact__lines { margin-top: 7px; font-size: 14.5px; line-height: 19px; }
  .contact__line { display: flex; justify-content: flex-end; align-items: center; gap: 6px; }
  .contact__icon { width: 12px; height: 12px; fill: var(--gold); }

  /* Back */
  .card--back {
    left: 320px; top: 493px;
    background: radial-gradient(ellipse at 48% 40%, var(--gold-center) 0%, #d8ba34 40%, var(--gold-deep) 100%);
  }
  .back__brand {
    position: absolute; left: 135px; top: 118px;
    display: flex; align-items: center; gap: 14px;
    color: var(--white);
  }
  .back__dot { width: 100px; height: 100px; border-radius: 50%; background: var(--white); }
  .back__text { margin-top: 10px; }
  .back__name { font-weight: 700; font-size: 40px; line-height: 1; letter-spacing: -0.5px; }
  .back__tagline { margin-top: 14px; font-size: 8.5px; font-weight: 700; letter-spacing: 1.6px; }
  .back__subline { margin-top: 3px; font-size: 6px; font-weight: 700; letter-spacing: 0.2px; }
  .back__url {
    position: absolute; left: 0; right: 0; top: 288px; text-align: center;
    font-size: 14px; letter-spacing: 4.6px; color: var(--white);
  }
</style>
</head>
<body>
<div class="canvas">

  <section class="card card--front">
    <div class="front__band"></div>
    <div class="brand">
      <div class="brand__row">
        <div class="brand__dot"></div>
        <div class="brand__text">
          <div class="brand__name">Levy Lantern</div>
          <div class="brand__tagline">TAX RELIEF. TAX RETURNS.</div>
          <div class="brand__subline">YOUR TRUSTED TAX ADVOCATES. PEACE OF MIND NATIONWIDE</div>
        </div>
      </div>
    </div>

    <div class="contact">
      <div class="contact__name">NORA WHITFIELD</div>
      <div class="contact__role">ATTORNEY</div>
      <div class="contact__address">4420 Orchard Ave. Ste 310<br>Riverside, CA 92506</div>
      <div class="contact__lines">
        <div class="contact__line">951-555-0148
          <svg class="contact__icon" viewBox="0 0 24 24"><path d="M6.6 10.8a15.1 15.1 0 0 0 6.6 6.6l2.2-2.2c.3-.3.7-.4 1-.2 1.1.4 2.3.6 3.6.6.6 0 1 .4 1 1V20c0 .6-.4 1-1 1A17 17 0 0 1 3 4c0-.6.4-1 1-1h3.5c.6 0 1 .4 1 1 0 1.3.2 2.5.6 3.6.1.3 0 .7-.2 1z"/></svg>
        </div>
        <div class="contact__line">nora@levylantern.com
          <svg class="contact__icon" viewBox="0 0 24 24"><path d="M2 5h20v2l-10 7L2 7z"/><path d="M2 9l10 7 10-7v10H2z"/></svg>
        </div>
        <div class="contact__line">www.levylantern.com
          <svg class="contact__icon" viewBox="0 0 24 24"><circle cx="12" cy="12" r="10"/><path d="M12 2a15 15 0 0 1 0 20M12 2a15 15 0 0 0 0 20M2 12h20" fill="none" stroke="#f7f7f5" stroke-width="1.5"/></svg>
        </div>
      </div>
    </div>
  </section>

  <section class="card card--back">
    <div class="back__brand">
      <div class="back__dot"></div>
      <div class="back__text">
        <div class="back__name">Levy Lantern</div>
        <div class="back__tagline">TAX RELIEF. TAX RETURNS.</div>
        <div class="back__subline">YOUR TRUSTED TAX ADVOCATES. PEACE OF MIND NATIONWIDE</div>
      </div>
    </div>
    <div class="back__url">www.levylantern.com</div>
  </section>

</div>
</body>
</html>
```